Dinner Invitation for an email

Please create an image I can embed in an email. The tone should be sophisticated, fun and festive.

Here is the copy:

FOOD | FRIENDS | FUN
Please join BRV and friends at Corvetti's Harbor House for cocktails, conversation and a delectable dinner
Date: Monday, January 23 (during OPMI)
Time: Cocktails start at 6:30 | Dinner is around 7
Place: Corvetti's Harbor House - The Pearl Terrace
27318 W Dunmore Pkwy - Scottsdale
(Adjacent to the Halvorsen Pinecrest Lodge)

RSVP: mara.quinby@brvholdco.example
(Mara will send you a calendar invite)

Hope to see you there!

```html
<!DOCTYPE html>
<html lang="en">
<head>
<meta charset="utf-8">
<title>BRV Dinner Invitation</title>
<link rel="stylesheet" href="https://fonts.googleapis.com/css2?family=Fredoka:wght@600;700&family=League+Spartan:wght@300;400;600&display=swap">
<style>
  :root {
    --night: #05070f;
    --deep-navy: #0a1432;
    --bar-blue: #1a3a8a;
    --drink-blue: #3f7fe0;
    --drink-glow: #8fc0ff;
    --ember: #b5481c;
    --headline: #8a86ff;
    --headline-glow: #5b3cff;
    --text: #e6ecff;
    --text-soft: #c9d3f2;
    --mark-blue: #2c4a9e;
  }
  * { margin: 0; padding: 0; box-sizing: border-box; }
  html, body {
    width: 803px;
    height: 1200px;
    overflow: hidden;
    background: var(--night);
  }
  .invitation {
    position: relative;
    width: 803px;
    height: 1200px;
    overflow: hidden;
    font-family: "League Spartan", "Helvetica Neue", Arial, sans-serif;
    color: var(--text);
  }
  .bar-scene {
    position: absolute;
    inset: 0;
    background:
      radial-gradient(ellipse 190px 240px at 405px 660px, var(--drink-glow) 0%, var(--drink-blue) 35%, rgba(30,70,170,0.6) 60%, rgba(10,20,50,0) 100%),
      radial-gradient(ellipse 420px 160px at 400px 200px, rgba(181,72,28,0.55) 0%, rgba(181,72,28,0) 100%),
      radial-gradient(ellipse 300px 200px at 700px 250px, rgba(181,72,28,0.35) 0%, rgba(181,72,28,0) 100%),
      linear-gradient(180deg, #120d12 0%, #1a1216 18%, var(--deep-navy) 40%, #0c1838 62%, #070a18 80%, var(--night) 100%);
  }
  .brand {
    position: absolute;
    top: 130px;
    left: 0;
    width: 803px;
    display: flex;
    justify-content: center;
    align-items: center;
    gap: 18px;
  }
  .brand-square {
    width: 44px;
    height: 44px;
    background: var(--mark-blue);
  }
  .brand-name {
    font-family: "League Spartan", "Helvetica Neue", Arial, sans-serif;
    font-weight: 600;
    font-size: 64px;
    line-height: 1;
    color: var(--text);
  }
  .headline {
    position: absolute;
    top: 292px;
    left: 0;
    width: 803px;
    text-align: center;
    font-family: "Fredoka", "Arial Rounded MT Bold", sans-serif;
    font-weight: 700;
    font-size: 60px;
    letter-spacing: 1px;
    color: var(--headline);
    text-shadow: 0 0 6px var(--headline-glow), 0 0 14px var(--headline-glow);
    transform: skewX(-8deg);
  }
  .intro {
    position: absolute;
    top: 383px;
    left: 0;
    width: 803px;
    text-align: center;
    font-weight: 300;
    font-size: 24px;
    line-height: 29px;
    color: var(--text-soft);
  }
  .details {
    position: absolute;
    top: 900px;
    left: 0;
    width: 803px;
    text-align: center;
    font-weight: 300;
    color: var(--text);
  }
  .details .date { font-size: 32px; line-height: 40px; }
  .details .line { font-size: 27px; line-height: 36px; }
  .details .note { font-size: 23px; line-height: 36px; }
  .rsvp {
    position: absolute;
    top: 1112px;
    left: 0;
    width: 803px;
    text-align: center;
    font-weight: 300;
    font-size: 18px;
    line-height: 21px;
    color: var(--text-soft);
  }
</style>
</head>
<body>
<main class="invitation">
  <div class="bar-scene" role="img" aria-label="Dim blurred cocktail bar with warm lights behind a glowing blue frothy cocktail garnished with dried flowers on the bar top"></div>

  <div class="brand">
    <span class="brand-square"></span>
    <span class="brand-name">BRV</span>
  </div>

  <h1 class="headline">FOOD | FRIENDS | FUN</h1>

  <p class="intro">Please join BRV and friends at Corvetti's Harbor House<br>for cocktails, conversation and a delectable dinner</p>

  <section class="details">
    <p class="date">Monday, January 23 (during OPMI)</p>
    <p class="line">Cocktails start at 6:30 | Dinner is around 7</p>
    <p class="line">Corvetti's Harbor House - The Pearl Terrace</p>
    <p class="line">27318 W Dunmore Pkwy - Scottsdale</p>
    <p class="note">(Adjacent to the Halvorsen Pinecrest Lodge)</p>
  </section>

  <p class="rsvp">RSVP: mara.quinby@brvholdco.example<br>(Mara will send you a calendar invite)</p>
</main>
</body>
</html>
```